Jolly Snaps - Photobooth hire

Photobooth flyer

We have just got our new photobooth and are ready to get the marketing side of things done! Our flyer needs to attract weddings, birthdays, corporate events, hens nights ect. For the winning flyer I would also like to follow up with the designer and get started with logo, business cards, web designs, car stickers etc. The flyer needs include this information

prices. $450 - 3 hrs $550 - 4 hrs $650 - 5 hrs. For extra time, additional payment can be made on the night. Our booths are also built with the flexibility to break down into smaller booths suitable for children. Prices start from $250 for kids parties and day time events.

All packages include
Unlimited prints
2 photo strips, one for you and one for friend.
Choice of different filters
Green screen technology - optional
Photobooth attendant
Use of cheeky props.

Call us for information and prices on additional items like photo albums, magnets, personalized photo strips, and more :)
0461927584

Feel free to change wording and add some character ;P

I would also like there to be sort of like a photostrip wave that I can add our photos. We will have them in a week :)
Thankyou for your time, am really looking forward to seeing what you come up with!!

Marketing

Sans Serif

8869ae

• I have uploaded a couple of flyers that I have come across and really like.. I like how the background is grey with some bold colour coming through.
• It also makes it hard because I don't have a logo.. But even in the heading, photobooth, I was thinking maybe a moustache underneath booth. Or even a cute little camera in one of the O's.

```html
<!DOCTYPE html>
<html lang="en">
<head>
<meta charset="utf-8">
<title>Jolly Snaps – Photobooth Hire Flyer</title>
<link rel="stylesheet" href="https://fonts.googleapis.com/css2?family=Amatic+SC:wght@700&family=Roboto+Condensed:wght@400;500&display=swap">
<style>
  :root {
    --page: #ffffff;
    --flyer-grey: #343434;
    --ink-light: #f4f4f4;
    --ink-dark: #1f1f1f;
    --strip-light: #e6e9e9;
    --strip-dark: #2f3a3a;
    --accent-purple: #8869ae;
    --panel-white: #f7f7f7;
  }
  * { box-sizing: border-box; margin: 0; padding: 0; }
  html, body {
    width: 1200px;
    height: 969px;
    overflow: hidden;
    background: var(--page);
  }
  .canvas {
    position: relative;
    width: 1200px;
    height: 969px;
  }
  .flyer {
    position: absolute;
    left: 178px;
    top: 54px;
    width: 628px;
    height: 897px;
    background: var(--flyer-grey);
    overflow: hidden;
    color: var(--ink-light);
    font-family: "Roboto Condensed", "Arial Narrow", sans-serif;
  }
  .film-strip {
    position: absolute;
    background: linear-gradient(90deg, var(--strip-light), #f2f4f4 50%, var(--strip-light));
  }
  .film-strip--vertical { left: 375px; top: 0; width: 158px; height: 306px; }
  .film-strip--horizontal { left: 0; top: 693px; width: 628px; height: 116px; }

  .brand {
    position: absolute;
    left: 40px;
    top: 90px;
    display: flex;
    align-items: center;
    gap: 16px;
  }
  .brand__dot {
    width: 38px;
    height: 38px;
    border-radius: 50%;
    background: var(--accent-purple);
  }
  .brand__name {
    font-family: "Amatic SC", "Arial Narrow", sans-serif;
    font-weight: 700;
    font-size: 84px;
    line-height: 1;
    color: var(--ink-light);
    white-space: nowrap;
  }

  .pricing {
    position: absolute;
    left: 30px;
    top: 306px;
    width: 570px;
    height: 130px;
  }
  .pricing__brace {
    position: absolute;
    top: -12px;
    font-family: "Amatic SC", sans-serif;
    font-weight: 700;
    font-size: 150px;
    line-height: 1;
    color: var(--ink-light);
  }
  .pricing__brace--open { left: 0; }
  .pricing__brace--close { right: 0; }
  .pricing__text {
    position: absolute;
    left: 55px;
    top: 12px;
    width: 490px;
    font-size: 16px;
    line-height: 22px;
  }

  .headline {
    position: absolute;
    left: 0;
    top: 424px;
    width: 610px;
    text-align: center;
    font-family: "Amatic SC", sans-serif;
    font-weight: 700;
    font-size: 72px;
    line-height: 1;
    letter-spacing: 2px;
    color: var(--ink-light);
  }

  .features {
    position: absolute;
    left: 39px;
    top: 498px;
    width: 529px;
    height: 150px;
    background: var(--panel-white);
    list-style: none;
    display: grid;
    grid-template-columns: 263px 1fr;
    grid-auto-rows: 35px;
    padding: 16px 0 0 19px;
    font-family: "Amatic SC", sans-serif;
    font-weight: 700;
    font-size: 24px;
    line-height: 35px;
    letter-spacing: 0.5px;
    color: var(--ink-dark);
  }

  .contact {
    position: absolute;
    left: 21px;
    top: 824px;
    width: 590px;
    font-size: 13.5px;
    font-weight: 500;
    line-height: 18px;
  }
</style>
</head>
<body>
<div class="canvas">
  <article class="flyer">
    <div class="film-strip film-strip--vertical" role="img" aria-label="Vertical film strip of photo frames"></div>

    <div class="brand">
      <span class="brand__dot"></span>
      <span class="brand__name">Jolly Snaps</span>
    </div>

    <section class="pricing">
      <span class="pricing__brace pricing__brace--open">{</span>
      <p class="pricing__text">$450 for 3 hrs, $550 for four hours<br>$650 for five hours. Our booths are also built with the flexibility to break down into smaller booths suitable for children. Prices start from $250 for kids parties and day time events.</p>
      <span class="pricing__brace pricing__brace--close">}</span>
    </section>

    <h1 class="headline">PHOTOBOOTH</h1>

    <ul class="features">
      <li>Unlimited prints</li>
      <li>Green screen technology</li>
      <li>2 photo strips</li>
      <li>Photobooth attendant</li>
      <li>Choice of filters</li>
      <li>Use of cheeky props.</li>
    </ul>

    <div class="film-strip film-strip--horizontal" role="img" aria-label="Horizontal film strip wave of photo frames"></div>

    <p class="contact">Call us for information and prices on additional items like photo albums, magnets, personalized photo strips, and more.<br>0461927584</p>
  </article>
</div>
</body>
</html>
```